Interior designer needs a gorgeous, chic business card design.

A new, small Interior Design firm needs a business card that is chic, contemporary and elegant. Nothing over the top. My interiors are contemporary classic with an elegant feel to them. I like to use quality finishes and products rather than follow the latest fads. Projects can be anything from Pre start selections, bathrooms, kitchens, bedrooms, custom upholstery, furniture, rugs and art etc. The final design should display quality and an achievable sense of chic. I am open to all colours including black but not limited to this.

```html
<!DOCTYPE html>
<html lang="en">
<head>
<meta charset="utf-8">
<title>Vela Studio – Business Card</title>
<link rel="stylesheet" href="https://fonts.googleapis.com/css2?family=Raleway:wght@300;400&display=swap">
<style>
  :root {
    --page-bg: #f2f3f3;
    --card-slate: #6e808a;
    --lattice-silver: #b7c1c6;
    --ink-light: #e9eef0;
    --ink-soft: #d3dbdf;
  }
  * { box-sizing: border-box; margin: 0; padding: 0; }
  html, body {
    width: 1200px;
    height: 800px;
    overflow: hidden;
    background: var(--page-bg);
  }
  .canvas {
    position: relative;
    width: 1200px;
    height: 800px;
  }
  .card {
    position: absolute;
    top: 250px;
    width: 520px;
    height: 297px;
    background: var(--card-slate);
    overflow: hidden;
    box-shadow: 0 10px 24px rgba(40, 55, 62, 0.18);
  }
  .card--front { left: 60px; }
  .card--back { left: 620px; }

  .lattice-band {
    position: absolute;
    left: 0;
    width: 100%;
    background: linear-gradient(90deg, #aab5ba, var(--lattice-silver) 50%, #aab5ba);
  }
  .card--front .lattice-band { top: 44px; height: 12px; }
  .card--back .lattice-band--upper { top: 0; height: 108px; }
  .card--back .lattice-band--lower { bottom: 0; height: 108px; }

  .wordmark {
    position: absolute;
    left: 0;
    width: 100%;
    display: flex;
    justify-content: center;
    align-items: center;
    gap: 10px;
    color: var(--ink-light);
    font-family: "Raleway", sans-serif;
    font-weight: 400;
    line-height: 1;
  }
  .wordmark__dot {
    display: block;
    border-radius: 50%;
    background: var(--ink-light);
  }
  .card--front .wordmark { top: 74px; font-size: 24px; }
  .card--front .wordmark__dot { width: 9px; height: 9px; }
  .card--back .wordmark { top: 131px; font-size: 30px; }
  .card--back .wordmark__dot { width: 11px; height: 11px; }

  .detail {
    position: absolute;
    font-family: "Raleway", sans-serif;
    font-weight: 300;
    color: var(--ink-soft);
    font-size: 11px;
    line-height: 1.5;
  }
  .contact-lines { left: 34px; top: 128px; }
  .person { left: 0; width: 100%; top: 136px; text-align: center; }
  .person__name { font-size: 15px; font-weight: 400; color: var(--ink-light); letter-spacing: 0.5px; }
  .person__role { font-size: 10px; }
  .website { left: 0; width: 100%; top: 206px; text-align: center; font-size: 12px; }
  .address { right: 40px; top: 236px; text-align: left; }
</style>
</head>
<body>
<main class="canvas">

  <section class="card card--front" aria-label="Business card front">
    <div class="lattice-band" role="img" aria-label="Silver interlocking lattice pattern strip"></div>
    <div class="wordmark">
      <span class="wordmark__dot"></span>
      <span class="wordmark__name">Vela Studio</span>
    </div>
    <div class="detail contact-lines">
      <p>000 111 222 333</p>
      <p>mail@mail.com</p>
    </div>
    <div class="detail person">
      <p class="person__name">Name Surname</p>
      <p class="person__role">Title</p>
    </div>
    <p class="detail website">www.velastudio.com</p>
    <div class="detail address">
      <p>Address Line 1</p>
      <p>Address Line 2</p>
    </div>
  </section>

  <section class="card card--back" aria-label="Business card back">
    <div class="lattice-band lattice-band--upper" role="img" aria-label="Wide silver interlocking lattice pattern band"></div>
    <div class="wordmark">
      <span class="wordmark__dot"></span>
      <span class="wordmark__name">Vela Studio</span>
    </div>
    <div class="lattice-band lattice-band--lower" role="img" aria-label="Wide silver interlocking lattice pattern band"></div>
  </section>

</main>
</body>
</html>
```